Brochure for The Lodge Nest a Vacation Rental company in Miami

The Lodge Nest is a vacation rental company in Miami. We specialize in vacation rentals and hotel-alternative rentals for travelers of all types.
We are looking for a modern and sleek brochure to help us promote our business and property management. This brochure will help persuade property owners to allow us to manage and operate their property as a vacation home.
We are looking for large images of luxury properties, modern sleek lines, modern text like "raleway" or "proxima nova" or something similar.
Target Market(s)
Property owners. We are a vacation rental management company.
Industry/Entity Type
Hotel
Font styles to use
Other font styles liked:
- Proxima nova or Raleway or brandon grotesque, or something similar
Requirements
Must have
- modern sleek design. Nice spacing and wonderful photos.
- Here's an example Brochure we liked in terms of design. Nothing to do with our industry, just the design style: http://www.quorvelhome.com/download/quorvel_brochure.pdf
- I HAVE INCLUDED THE FOLLOWING FILES:
- - logo files
- - screen shots of website designs that I like for design inspiration
- - content you can use for the brochure about our company and other information etc
- - images of properties we manage

```html
<!DOCTYPE html>
<html lang="en">
<head>
<meta charset="utf-8">
<title>The Lodge Nest – Owner Brochure</title>
<link href="https://fonts.googleapis.com/css2?family=Raleway:wght@400;500;600;700;800&display=swap" rel="stylesheet">
<style>
:root{
  --bg:#e9e9e9;
  --paper:#ffffff;
  --ink:#3a3a3a;
  --ink-soft:#6e6e6e;
  --band:#8c8c8c;
  --band-dark:#4a4a4a;
  --rule:#bdbdbd;
  --tint:#f3f3f3;
  --pool:#58b9d6;
  --sky:#a9c9de;
  --glass:#6f8797;
  --night:#2a3a4a;
}
*{box-sizing:border-box;margin:0;padding:0}
html,body{width:1200px;height:2368px;overflow:hidden;background:var(--bg);font-family:"Raleway",sans-serif;color:var(--ink)}
.spread{position:absolute;left:40px;width:1120px;height:700px;background:var(--paper);display:flex;box-shadow:0 6px 22px rgba(0,0,0,.18)}
.spread--cover{top:50px}
.spread--owners{top:834px}
.spread--offer{top:1618px}
.page{position:relative;width:560px;height:700px;overflow:hidden}
.page + .page{border-left:1px solid #e2e2e2}
.photo{position:absolute}
.photo--pool{background:linear-gradient(180deg,var(--sky) 0%,#cfdfe8 35%,#6f9a78 48%,var(--pool) 60%,#2f93b8 100%)}
.photo--tower{background:linear-gradient(160deg,#d8e6f0 0%,var(--sky) 35%,var(--glass) 70%,#55707f 100%)}
.photo--night{background:linear-gradient(180deg,#1c2633 0%,var(--night) 45%,#3e6f86 80%,#4fa6c4 100%)}
.photo--interior{background:linear-gradient(160deg,#f1eee9 0%,#d9d3ca 55%,#a9a195 100%)}
.brand{position:absolute;display:flex;align-items:center;gap:8px;font-weight:700;font-size:17px;letter-spacing:.12em;text-transform:uppercase;color:var(--ink)}
.brand__dot{width:10px;height:10px;background:var(--ink)}
.tagline{position:absolute;left:30px;right:30px;top:470px;height:44px;border:1px solid var(--band-dark);display:flex;align-items:center;justify-content:center;font-weight:700;font-size:15px;letter-spacing:.12em}
.intro{position:absolute;left:50px;right:50px;top:530px;text-align:center;font-size:13px;line-height:1.6;color:var(--ink-soft)}
.heading{font-weight:800;text-transform:uppercase;letter-spacing:.04em;color:var(--ink)}
.sub{font-weight:700;font-size:13px;margin-top:14px;color:var(--ink)}
.body{font-size:11.5px;line-height:1.6;color:var(--ink-soft);margin-top:4px}
.col{position:absolute}
.owners{left:40px;right:40px;top:60px}
.owners .heading{font-size:24px;line-height:1.2}
.owners .heading--small{font-size:20px;margin-top:30px}
.owners .rule{height:2px;width:60px;background:var(--band);margin:10px 0 14px}
.offer-text{left:30px;top:40px;width:320px}
.offer-text .heading{font-size:20px;margin-top:22px}
.offer-text .heading:first-child{margin-top:0}
.offer-photos{position:absolute;left:370px;top:40px;width:160px}
.offer-photos .photo{position:relative;height:190px;margin-bottom:14px}
.tab{position:absolute;right:0;top:40px;width:230px;height:40px;background:var(--band-dark);color:#fff;font-weight:700;font-size:16px;letter-spacing:.12em;display:flex;align-items:center;padding-left:24px}
.travel{left:40px;right:40px;top:110px}
.travel .heading{font-size:22px}
.travel .sub{text-transform:uppercase;letter-spacing:.05em;margin-top:18px}
.side-band{position:absolute;left:0;top:0;width:24px;height:700px;background:var(--tint)}
</style>
</head>
<body>

<!-- Cover spread -->
<section class="spread spread--cover">
  <div class="page">
    <div class="brand" style="left:30px;top:30px"><span class="brand__dot"></span>The Lodge Nest</div>
    <div class="photo photo--pool" role="img" aria-label="Resort pool deck with palm trees and a high-rise behind" style="left:0;top:90px;width:560px;height:610px"></div>
  </div>
  <div class="page" style="background:var(--tint)">
    <div class="brand" style="left:210px;top:30px"><span class="brand__dot"></span>The Lodge Nest</div>
    <div class="photo photo--tower" role="img" aria-label="Glass residential tower seen from a balcony" style="left:30px;top:90px;width:500px;height:360px"></div>
    <div class="tagline">CREATING A PERSONALIZED TRAVEL EXPERIENCE</div>
    <p class="intro">We specialize in vacation rentals and hotel-alternative rentals for travelers of all types.</p>
  </div>
</section>

<!-- Owners spread -->
<section class="spread spread--owners">
  <div class="page">
    <div class="photo photo--night" role="img" aria-label="City towers at night above a lit pool" style="left:0;top:0;width:560px;height:360px"></div>
    <div class="photo photo--pool" role="img" aria-label="Pool terrace with palms and sun loungers" style="left:0;top:370px;width:560px;height:330px"></div>
  </div>
  <div class="page">
    <div class="col owners">
      <h2 class="heading">Owners:<br>Become a Partner</h2>
      <div class="rule"></div>
      <p class="body">As an owner of a luxury property in a vacation destination you understand the value of every booked night. Partnering with The Lodge Nest is the most effective way to maximize the return on your vacation investment.</p>
      <p class="body">At The Lodge Nest we know that your home deserves more than a listing. We combine hotel-grade service with careful management so that guests return and your property earns year round.</p>
      <p class="body">Are you interested in working with The Lodge Nest?</p>
      <h3 class="heading heading--small">Why Become Our Partner:</h3>
      <div class="rule"></div>
      <p class="sub">Selection Process:</p>
      <p class="body">Of the hundreds and hundreds of properties, we accept less than 20% of the homes that we evaluate. With a strict selection process, we ensure that each of our homes meets a high standard.</p>
      <p class="sub">Pay-for-Performance Model:</p>
      <p class="body">We’re successful when you’re successful. With no annual subscriptions, fees or set-up charges, you only pay when your property earns money.</p>
      <p class="sub">We Take Care of the Details:</p>
      <p class="body">We’ll handle the work needed to get to know you, your property and your preferences. Then we take care of everything from cleaning to guest care.</p>
    </div>
  </div>
</section>

<!-- Offer / travelers spread -->
<section class="spread spread--offer">
  <div class="page">
    <div class="col offer-text">
      <h2 class="heading">What We Offer</h2>
      <p class="body">We’re a data-inspired luxury hospitality company that provides you with a turnkey management and booking system. We’re experts in operating and marketing homes for guests who expect the comfort of a hotel.</p>
      <h2 class="heading">Full Service Solution</h2>
      <p class="body">The Lodge Nest Concierge Team provides white-glove management of every stay. From preparation to checkout we handle cleaning, maintenance, linens and guest messaging, so your property is always ready. We work to deliver five-star reviews and consistently strong occupancy for our owners.</p>
      <h2 class="heading">Professional Marketing Team</h2>
      <p class="body">We’ve assembled a team of marketing experts in photography, copywriting and design. Using cutting-edge tools, we list your home on top booking sites and adjust pricing daily to reach the best guests.</p>
    </div>
    <div class="offer-photos">
      <div class="photo photo--pool" role="img" aria-label="Rooftop pool with city view"></div>
      <div class="photo photo--interior" role="img" aria-label="Bright living room interior"></div>
      <div class="photo photo--tower" role="img" aria-label="Bedroom with floor-to-ceiling windows"></div>
    </div>
  </div>
  <div class="page">
    <div class="side-band"></div>
    <div class="tab">TRAVELERS:</div>
    <div class="col travel">
      <h2 class="heading">Why Travelers Choose Us:</h2>
      <p class="sub">Luxury Properties</p>
      <p class="body">Our clients receive the best homes in the most desirable locations in Miami, each selected for comfort and style.</p>
      <p class="sub">24/7 Guest Support</p>
      <p class="body">If you need a question answered at any hour, our Guest Relations team is available by phone or message around the clock.</p>
      <p class="sub">Price Competitiveness</p>
      <p class="body">Why book low quality and guest rooms as a hotel? With our homes, guests get more space for a fair and honest price.</p>
      <p class="sub">The Lodge Nest Experience</p>
      <p class="body">We do more than hand over the keys. Our team creates a personalized experience, from local tips to arrival setup, making every trip unique and memorable.</p>
    </div>
  </div>
</section>

</body>
</html>
```